依頼概要
■依頼の目的/概要
弊社ではあささんぽ、あさひを浴びようと思えるSNSアプリの制作を行っております。
ほしぞらノートアプリでは毎日の記録をつけるためのライフログ系の機能を制作しております。

ライフログとして自分の記録を見返したり、他のユーザーからも見てもらえる機能がある日記のデザイン及びその画面のUI制作をお願いします。

■依頼の詳細
ユーザーが投稿するのは朝日を含めた毎朝の日記で自分のほしぞらノート(本のテイスト)の左ページを投稿します(アプリ上ホーム画面)。その日記投稿や朝散歩をすればするほど幸せの証として「きらりリボン」を報酬として獲得し、毎朝獲得したハートを自分のほしぞらノートの右ページに貯めておけます(アプリ上ほしぞらノート画面)。

今回トライアルでお願いしたいのはユーザーが朝日を投稿するホーム画面のUIです(左ページ)。
必要な要項といたしましては、
・ユーザーが撮影した朝日の写真(必須)
・日付(必須)
・天気※
・場所※
・気温※
・日記コメント※
・自分のキャラクター(こちらは素材があります)※

を入れられるようにしたいと考えております。
※は、ユーザー任意で入れたり、非表示にできます

スワイプすると、他のユーザーの日記のページをめくるような感覚のモーションの検討もしています。

こちらをトライアルという形で、採用された方には別画面/別バージョンの本のデザインや詳細なUIなどご相談したいと考えております。追加のUIのお見積りなども含め、ご提案いただけますと幸いです。

現在の開発中の仮デザインを添付しますが、よりよいデザインを是非、応募いただけますと幸いです。

画面UIのデザインがイメージと合っていた為。

この度、ご提案いただきありがとうございました。ご厚情にお応えすることができず、誠に申し訳ございません。勝手ではございますが、これに懲りず今後ともお付き合いくださいますようお願い申し上げます。

```html
<!DOCTYPE html>
<html lang="ja">
<head>
<meta charset="utf-8">
<title>ほしぞらノート ホーム</title>
<link href="https://fonts.googleapis.com/css2?family=Noto+Sans+JP:wght@400;500;700&display=swap" rel="stylesheet">
<style>
  :root{
    --ink:#222222;
    --muted:#9a9a9a;
    --rule:#d9d9d9;
    --page:#ffffff;
    --frame:#ececec;
    --teal:#3f9e86;
    --teal-dark:#2f7f6b;
    --heart:#ef6b6b;
    --avatar:#f2b52a;
    --tabbar:#555555;
    --tabbar-foot:#e9e9e9;
    --photo-top:#9dbad8;
    --photo-bottom:#c4c2bb;
  }
  *{margin:0;padding:0;box-sizing:border-box;}
  html,body{width:1200px;height:2596px;overflow:hidden;background:var(--page);}
  body{font-family:"Noto Sans JP",sans-serif;color:var(--ink);position:relative;}
  .abs{position:absolute;}

  .status-bar{left:0;top:0;width:1200px;height:150px;}
  .status-time{left:64px;top:34px;font-size:44px;font-weight:500;}
  .status-icons{right:56px;top:40px;}

  .app-header{left:0;top:150px;width:1200px;height:142px;border-bottom:3px solid var(--rule);}
  .brand{left:64px;top:34px;font-size:64px;font-weight:700;letter-spacing:2px;}
  .avatar{left:780px;top:24px;width:100px;height:100px;border-radius:50%;background:var(--avatar);}
  .bell{left:920px;top:34px;}
  .menu{left:1036px;top:44px;}

  .meter{left:0;top:292px;width:1200px;height:228px;border-bottom:12px solid var(--frame);}
  .meter-heart{left:62px;top:110px;}
  .meter-title{left:168px;top:30px;font-size:40px;font-weight:700;}
  .meter-track{left:168px;top:106px;width:864px;height:44px;border-radius:22px;border:4px solid var(--rule);background:#f4f4f4;}
  .meter-fill{left:164px;top:102px;width:700px;height:48px;border-radius:24px;background:var(--teal);}
  .meter-caption{right:168px;top:168px;font-size:30px;color:#555;}

  .journal-card{left:0;top:520px;width:1200px;height:1848px;border-left:10px solid var(--frame);border-right:10px solid var(--frame);}
  .date-row{left:0;top:0;width:1180px;height:184px;}
  .date-day{left:56px;top:78px;font-size:40px;}
  .date-main{left:136px;top:36px;font-size:52px;font-weight:500;}
  .date-main b{font-size:92px;font-weight:500;}
  .calendar{left:510px;top:62px;}
  .pin{left:650px;top:60px;}
  .place{left:706px;top:64px;font-size:44px;}
  .weather{left:1020px;top:50px;width:96px;height:96px;border-radius:50%;border:4px solid var(--rule);}

  .sunrise-photo{left:-10px;top:184px;width:1200px;height:1196px;
    background:linear-gradient(180deg,var(--photo-top) 0%,var(--photo-bottom) 100%);}
  .add-photo{left:1000px;top:1180px;width:128px;height:128px;border-radius:50%;background:#fff;}

  .notes{left:0;top:1380px;width:1180px;height:468px;}
  .notes-label{left:56px;top:54px;font-size:44px;color:var(--muted);}
  .notes-line{left:56px;width:1070px;height:3px;background:var(--rule);}
  .page-turn{right:100px;top:406px;font-size:30px;color:var(--muted);}
  .page-curl{right:0;bottom:0;}

  .tab-bar{left:0;top:2368px;width:1200px;height:160px;background:var(--tabbar);color:#fff;}
  .tab{top:0;width:240px;height:160px;text-align:center;}
  .tab svg{margin-top:22px;}
  .tab span{display:block;font-size:28px;margin-top:4px;}
  .home-indicator{left:0;top:2528px;width:1200px;height:68px;background:var(--tabbar-foot);}
</style>
</head>
<body>
  <div class="status-bar abs">
    <div class="status-time abs">1:20</div>
    <svg class="status-icons abs" width="200" height="40" viewBox="0 0 200 40">
      <rect x="0" y="24" width="8" height="12" fill="#bbb"/><rect x="14" y="18" width="8" height="18" fill="#bbb"/>
      <rect x="28" y="12" width="8" height="24" fill="#bbb"/><rect x="42" y="6" width="8" height="30" fill="#ccc"/>
      <path d="M74 14 Q96 -4 118 14 M82 22 Q96 10 110 22" stroke="#bbb" stroke-width="5" fill="none"/><circle cx="96" cy="30" r="5" fill="#bbb"/>
      <rect x="136" y="6" width="54" height="28" rx="6" fill="none" stroke="#bbb" stroke-width="3"/><rect x="141" y="11" width="40" height="18" rx="3" fill="#bbb"/>
    </svg>
  </div>

  <header class="app-header abs">
    <div class="brand abs">LOGO</div>
    <div class="avatar abs" role="img" aria-label="ユーザーのキャラクター"></div>
    <svg class="bell abs" width="80" height="80" viewBox="0 0 80 80">
      <path d="M20 56 L20 34 Q20 14 40 14 Q60 14 60 34 L60 56 Z M14 56 H66" stroke="#333" stroke-width="6" fill="none" stroke-linejoin="round"/>
      <path d="M33 64 Q40 72 47 64" stroke="#333" stroke-width="6" fill="none"/>
      <circle cx="62" cy="14" r="9" fill="var(--heart)"/>
    </svg>
    <svg class="menu abs" width="84" height="60" viewBox="0 0 84 60">
      <rect x="0" y="0" width="84" height="8" rx="4" fill="#333"/><rect x="0" y="26" width="84" height="8" rx="4" fill="#333"/><rect x="0" y="52" width="84" height="8" rx="4" fill="#333"/>
    </svg>
  </header>

  <section class="meter abs">
    <svg class="meter-heart abs" width="72" height="64" viewBox="0 0 72 64">
      <path d="M36 62 L6 32 Q-6 16 8 6 Q24 -4 36 14 Q48 -4 64 6 Q78 16 66 32 Z" fill="var(--heart)"/>
    </svg>
    <div class="meter-title abs">きらりリボンメーター</div>
    <div class="meter-track abs"></div>
    <div class="meter-fill abs"></div>
    <div class="meter-caption abs">ほしぞらノート連続３日目</div>
  </section>

  <main class="journal-card abs">
    <div class="date-row abs">
      <div class="date-day abs">Day</div>
      <div class="date-main abs"><b>3</b>月<b>15</b>日(水)</div>
      <svg class="calendar abs" width="60" height="60" viewBox="0 0 60 60">
        <rect x="4" y="10" width="52" height="46" rx="4" fill="none" stroke="var(--teal)" stroke-width="5"/>
        <path d="M4 24 H56 M18 2 V16 M42 2 V16" stroke="var(--teal)" stroke-width="5"/>
        <rect x="14" y="32" width="8" height="8" fill="var(--teal)"/><rect x="26" y="32" width="8" height="8" fill="var(--teal)"/><rect x="38" y="32" width="8" height="8" fill="var(--teal)"/>
      </svg>
      <svg class="pin abs" width="44" height="60" viewBox="0 0 44 60">
        <path d="M22 58 Q2 32 2 22 A20 20 0 0 1 42 22 Q42 32 22 58 Z" fill="none" stroke="#333" stroke-width="5"/>
        <circle cx="22" cy="22" r="7" fill="#333"/>
      </svg>
      <div class="place abs">Kasumi Bay</div>
      <div class="weather abs">
        <svg width="88" height="88" viewBox="0 0 88 88">
          <path d="M18 62 Q8 62 8 52 Q8 42 20 42 Q22 28 38 28 Q50 28 54 38 Q70 36 72 50 Q76 62 64 62 Z" fill="var(--teal)"/>
          <path d="M40 40 Q48 24 64 30 Q76 36 74 50" fill="none" stroke="var(--teal-dark)" stroke-width="4"/>
        </svg>
      </div>
    </div>

    <div class="sunrise-photo abs" role="img" aria-label="ユーザーが撮影した朝日の写真"></div>
    <div class="add-photo abs">
      <svg width="128" height="128" viewBox="0 0 128 128">
        <rect x="32" y="44" width="62" height="46" rx="6" fill="var(--teal)"/>
        <rect x="50" y="36" width="24" height="12" rx="3" fill="var(--teal)"/>
        <circle cx="63" cy="67" r="12" fill="#fff"/><circle cx="63" cy="67" r="7" fill="var(--teal)"/>
        <circle cx="92" cy="42" r="14" fill="#fff"/>
        <path d="M92 32 V52 M82 42 H102" stroke="var(--teal)" stroke-width="5"/>
      </svg>
    </div>

    <section class="notes abs">
      <div class="notes-label abs">朝のできごと</div>
      <div class="notes-line abs" style="top:128px"></div>
      <div class="notes-line abs" style="top:204px"></div>
      <div class="notes-line abs" style="top:276px"></div>
      <div class="notes-line abs" style="top:344px"></div>
      <div class="page-turn abs">ページをめくる</div>
      <svg class="page-curl abs" width="80" height="80" viewBox="0 0 80 80">
        <path d="M80 0 L80 80 L0 80 Z" fill="#f2f2f2"/>
        <path d="M80 0 Q46 40 0 80 L40 44 Z" fill="#dcdcdc" stroke="#bbb" stroke-width="2"/>
      </svg>
    </section>
  </main>

  <nav class="tab-bar abs">
    <div class="tab abs" style="left:0">
      <svg width="76" height="72" viewBox="0 0 76 72">
        <path d="M6 34 L38 6 L70 34 M14 28 V66 H62 V28 M30 66 V46 H46 V66" stroke="#fff" stroke-width="6" fill="none" stroke-linejoin="round"/>
      </svg>
      <span>ホーム</span>
    </div>
    <div class="tab abs" style="left:480px">
      <svg width="110" height="72" viewBox="0 0 110 72">
        <circle cx="36" cy="20" r="14" stroke="#fff" stroke-width="5" fill="none"/>
        <path d="M8 68 Q8 40 36 40 Q64 40 64 68" stroke="#fff" stroke-width="5" fill="none"/>
        <circle cx="74" cy="20" r="14" stroke="#fff" stroke-width="5" fill="none"/>
        <path d="M58 42 Q66 40 74 40 Q102 40 102 68" stroke="#fff" stroke-width="5" fill="none"/>
      </svg>
      <span>お友達</span>
    </div>
    <div class="tab abs" style="left:972px">
      <svg width="72" height="72" viewBox="0 0 72 72">
        <circle cx="36" cy="36" r="22" stroke="#fff" stroke-width="6" fill="none" stroke-dasharray="10 7"/>
        <circle cx="36" cy="36" r="12" stroke="#fff" stroke-width="5" fill="none"/>
      </svg>
      <span>設定</span>
    </div>
  </nav>
  <div class="home-indicator abs"></div>
</body>
</html>
```